Business Card needed for Drainor, a growing Septic Service company

Drainor, a growing local septic service company in Pennsylvania, needs updated business cards. We'd like the business card to feature our logo and communicate that we provide Septic Pumping, Installations/Repairs, Restroom Rentals, and 24/7 Emergency Service. The business card should be eye-catching, bold, and clean/simple. We have been in business almost 10 years and would like to expand and update our business brand and image.

Target Market(s)

Residential and Commercial, New and Current Homeowners

Industry/Entity Type

Service

Contact Information for Business Card

Contact on the business card should be: Dean Harlow Owner & Operator
Phone: 555-555-0187
Email: service@drainor-example.com
Website: www.drainor-example.com
Address: 812 Millbrook Lane Alderbury ZZ 00000

Font styles to use
Sans Serif

Colors

Designer to choose colors to be used in the design.

Requirements
Must have
• Feature logo on both side of business card.
Nice to have
• We envision the contact information on one side and our services listed on the other side. Utilize the green from the symbol in our logo as part of the design, overall design color scheme should be white, grey, black.

```html
<!DOCTYPE html>
<html lang="en">
<head>
<meta charset="utf-8">
<title>Drainor Business Card</title>
<link href="https://fonts.googleapis.com/css2?family=Barlow:wght@400;500;700&display=swap" rel="stylesheet">
<style>
  :root {
    --backdrop: #e9eaea;
    --card-black: #1b1b1b;
    --card-black-deep: #111111;
    --brand-green: #80ff00;
    --ink: #111111;
    --paper: #ffffff;
  }
  * { margin: 0; padding: 0; box-sizing: border-box; }
  html, body { width: 1200px; height: 2400px; overflow: hidden; }
  body {
    background: var(--backdrop);
    font-family: "Barlow", Arial, sans-serif;
    position: relative;
  }
  .card {
    position: absolute;
    left: 255px;
    width: 690px;
    height: 393px;
    background: linear-gradient(180deg, var(--card-black) 0%, var(--card-black-deep) 100%);
    overflow: hidden;
  }
  .card--services { top: 77px; }
  .card--contact { top: 570px; }

  .brand {
    position: absolute;
    display: flex;
    align-items: center;
    gap: 10px;
  }
  .brand__square {
    width: 58px; height: 58px;
    background: var(--brand-green);
  }
  .brand__name {
    font-weight: 700;
    font-size: 60px;
    letter-spacing: 3px;
    color: var(--paper);
    text-transform: uppercase;
    line-height: 1;
  }
  .card--services .brand { left: 230px; top: 35px; }
  .card--contact .brand { left: 79px; top: 34px; }

  .band {
    position: absolute;
    background: var(--brand-green);
  }
  .card--services .band { left: 0; top: 110px; width: 582px; height: 206px; }
  .card--contact .band { left: 72px; top: 109px; width: 618px; height: 206px; }

  .services__title {
    position: absolute; left: 197px; top: 0;
    font-size: 37px; font-weight: 500; color: var(--ink);
  }
  .service-list {
    position: absolute; right: 237px; top: 46px;
    list-style: none; text-align: right;
  }
  .service-list li {
    display: flex; align-items: center; justify-content: flex-end; gap: 10px;
    font-size: 21px; font-weight: 500; color: var(--paper);
    height: 38px;
  }
  .service-list svg { width: 46px; height: 28px; }

  .person__name {
    position: absolute; left: 274px; top: 2px;
    font-size: 37px; font-weight: 500; color: var(--ink);
  }
  .person__role {
    position: absolute; left: 274px; top: 46px;
    font-size: 27px; font-weight: 500; color: var(--paper); letter-spacing: 1px;
  }
  .contact-list {
    position: absolute; left: 274px; top: 106px; list-style: none;
  }
  .contact-list li {
    display: flex; align-items: center; gap: 8px;
    font-size: 18px; font-weight: 500; color: var(--paper); letter-spacing: 0.5px;
    height: 30px;
  }
  .contact-list svg { width: 20px; height: 20px; }
  .website {
    position: absolute; left: 69px; top: 332px;
    font-size: 20px; font-weight: 500; color: var(--paper); letter-spacing: 0.5px;
  }
</style>
</head>
<body>

<section class="card card--services" aria-label="Services side">
  <div class="brand"><span class="brand__square"></span><span class="brand__name">Drainor</span></div>
  <div class="band">
    <h2 class="services__title">Services</h2>
    <ul class="service-list">
      <li>Septic Pumping
        <svg viewBox="0 0 46 28" fill="none" stroke="#fff" stroke-width="2"><rect x="14" y="5" width="28" height="13" rx="6"/><path d="M2 18h12V9H7l-5 6z"/><circle cx="9" cy="22" r="3"/><circle cx="28" cy="22" r="3"/><circle cx="37" cy="22" r="3"/></svg></li>
      <li>Restroom Rentals
        <svg viewBox="0 0 46 28" fill="none" stroke="#fff" stroke-width="2"><rect x="15" y="1" width="16" height="26" rx="5"/></svg></li>
      <li>Installations/Repairs
        <svg viewBox="0 0 46 28" fill="none" stroke="#fff" stroke-width="2"><path d="M10 14h18a9 9 0 0 1-18 0zM16 22v5h10"/><rect x="30" y="2" width="6" height="12"/></svg></li>
      <li>24/7 Emergency Service.
        <svg viewBox="0 0 46 28" fill="none" stroke="#fff" stroke-width="2"><circle cx="23" cy="14" r="11"/><path d="M23 8v6l4 3"/></svg></li>
    </ul>
  </div>
</section>

<section class="card card--contact" aria-label="Contact side">
  <div class="brand"><span class="brand__square"></span><span class="brand__name">Drainor</span></div>
  <div class="band">
    <h1 class="person__name">Dean Harlow</h1>
    <p class="person__role">Owner &amp; Operator</p>
    <ul class="contact-list">
      <li><svg viewBox="0 0 20 20" fill="none" stroke="#fff" stroke-width="1.6"><circle cx="10" cy="10" r="8.5"/><path d="M7 6l2 2-1 1.5a6 6 0 0 0 2.5 2.5L12 11l2 2-1.5 1.5C9 14 6 11 5.5 7.5z"/></svg>555-555-0187</li>
      <li><svg viewBox="0 0 20 20" fill="none" stroke="#fff" stroke-width="1.6"><circle cx="10" cy="10" r="8.5"/><circle cx="10" cy="10" r="3.5"/></svg>service@drainor-example.com</li>
      <li><svg viewBox="0 0 20 20" fill="none" stroke="#fff" stroke-width="1.6"><path d="M10 18s-6-6-6-10a6 6 0 0 1 12 0c0 4-6 10-6 10z"/><circle cx="10" cy="8" r="2"/></svg>812 Millbrook Lane Alderbury ZZ 00000</li>
    </ul>
  </div>
  <p class="website">www.drainor-example.com</p>
</section>

</body>
</html>
```